New Business Card Design Project

The look of the business cards should include
-Clean Lines
-Should suit a sophisticated customer
-Evoke a mix of business and creativity
-Incorporate the color Gray or Black:White palette
-Open to see layouts in both vertical and horizontal
3 partners (we need 3 cards)
DORENE VASK
ELKE TARNOWSKI
NENA QUASTIGO
Reason: We would like more submissions please
Target Market(s)
We are a NYC and European based boutique consulting agency specializing in fashion business and creative clients. In addition to consulting we will be offering an e-commerce site selling women’s accessories and jewelry geared towards fashion forward women ages 25-50.
Industry/Entity Type
Business
Requirements
Must have
- - texture
- grayscale
3 Partners
Details for each card
CONSULTING I DESIGN
NENA QUASTIGO
Founding Partner
646.208.3371
nenA@themarlowtidecollective.com
www.themarlowtidecollective.com
CONSULTING I DESIGN
DORENE VASK
Founding Partner
646.851.2907
dorene@themarlowtidecollective.com
www.themarlowtidecollective.com
CONSULTING I DESIGN
Elke Dunsford Tarnowski
Founding Partner
(no phone for her)
Elke@themarlowtidecollective.com
www.themarlowtidecollective.com

```html
<!DOCTYPE html>
<html lang="en">
<head>
<meta charset="utf-8">
<title>The Marlow Tide Collective – Business Cards</title>
<link href="https://fonts.googleapis.com/css2?family=Arimo:wght@400&display=swap" rel="stylesheet">
<style>
  :root {
    --page: #ffffff;
    --card: #333333;
    --ink: #ffffff;
    --rule: #3f3f3f;
  }
  html, body {
    margin: 0;
    padding: 0;
    width: 1200px;
    height: 1000px;
    overflow: hidden;
    background: var(--page);
  }
  .canvas {
    position: relative;
    width: 1200px;
    height: 1000px;
    font-family: "Arimo", Arial, sans-serif;
    color: var(--ink);
  }
  .card {
    position: absolute;
    width: 625px;
    height: 385px;
    background: var(--card);
  }
  .card--front { left: 101px; top: 101px; }
  .card--back  { left: 468px; top: 513px; }

  .divider {
    position: absolute;
    left: 334px;
    top: 60px;
    width: 1px;
    height: 264px;
    background: var(--rule);
  }

  .contact {
    position: absolute;
    left: 73px;
    top: 143px;
  }
  .contact__name {
    font-size: 18px;
    line-height: 20px;
    margin: 0;
    font-weight: 400;
  }
  .contact__role {
    font-size: 13px;
    letter-spacing: 1px;
    margin: 2px 0 10px;
  }
  .contact__line {
    display: flex;
    align-items: center;
    gap: 8px;
    font-size: 15px;
    height: 24px;
  }
  .contact__line--email { font-size: 14px; letter-spacing: -0.1px; }
  .contact__icon { width: 24px; display: flex; justify-content: center; }

  .wordmark {
    position: absolute;
    width: 200px;
    text-align: center;
    font-size: 20px;
    line-height: 40px;
    letter-spacing: 5px;
    text-transform: uppercase;
  }
  .card--front .wordmark { left: 362px; top: 98px; }
  .card--back .wordmark  { left: 212px; top: 102px; }

  .tagline {
    position: absolute;
    left: 362px;
    top: 293px;
    width: 200px;
    text-align: center;
    font-size: 10px;
    letter-spacing: 2.6px;
  }
  .website {
    position: absolute;
    left: 162px;
    top: 311px;
    width: 300px;
    text-align: center;
    font-size: 11.5px;
    letter-spacing: 1.6px;
  }
</style>
</head>
<body>
<main class="canvas">
  <section class="card card--front" aria-label="Card front">
    <div class="contact">
      <h1 class="contact__name">NENA QUASTIGO</h1>
      <div class="contact__role">Founding Partner</div>
      <div class="contact__line">
        <span class="contact__icon">
          <svg width="12" height="20" viewBox="0 0 12 20" aria-hidden="true">
            <rect x="1" y="1" width="10" height="18" rx="1.5" fill="none" stroke="#fff" stroke-width="1.5"/>
            <rect x="3" y="3.5" width="6" height="7" fill="#fff"/>
            <g fill="#fff"><rect x="3" y="12.5" width="1.6" height="1.2"/><rect x="5.2" y="12.5" width="1.6" height="1.2"/><rect x="7.4" y="12.5" width="1.6" height="1.2"/><rect x="3" y="15" width="1.6" height="1.2"/><rect x="5.2" y="15" width="1.6" height="1.2"/><rect x="7.4" y="15" width="1.6" height="1.2"/></g>
          </svg>
        </span>
        <span>646.208.3371</span>
      </div>
      <div class="contact__line contact__line--email">
        <span class="contact__icon">
          <svg width="26" height="16" viewBox="0 0 26 16" aria-hidden="true">
            <rect x="0.5" y="0.5" width="25" height="15" fill="#fff"/>
            <polyline points="0.5,0.8 13,9.5 25.5,0.8" fill="none" stroke="#333" stroke-width="1.2"/>
            <line x1="0.5" y1="15.5" x2="10" y2="7.5" stroke="#333" stroke-width="1"/>
            <line x1="25.5" y1="15.5" x2="16" y2="7.5" stroke="#333" stroke-width="1"/>
          </svg>
        </span>
        <span>nenA@themarlowtidecollective.com</span>
      </div>
    </div>
    <div class="divider"></div>
    <div class="wordmark">The<br>Marlow<br>Tide<br>Collective</div>
    <div class="tagline">CONSULTING I DESIGN</div>
  </section>

  <section class="card card--back" aria-label="Card back">
    <div class="wordmark">The<br>Marlow<br>Tide<br>Collective</div>
    <div class="website">www.themarlowtidecollective.com</div>
  </section>
</main>
</body>
</html>
```